Business card design needed

We are a independent software development company specialising in financial and business custom applications and Verlane Suite automation and integration.
Colours: Blue/Purple/Yellow/White
Target Market(s)
CFO's, CIO's, Financial Managers, Business Managers
Industry/Entity Type
Financial
Contact Information for Business Card
Dennis P Holtby
MR Systems (QLD) Pty Ltd
ABN: 64 905 218 473
PO Box 817
Harwick Point Qld 4619
Mobile: 0412 739 064
Email: programmer@mr-systems.example
Web: www.mr-systems.example
Brevlo logo, Plazzo logo
Logo styles of interest
Abstract Logo
Requirements
Must have
- Flat screen computer monitor keyboard and mouse
Nice to have
- would like to see some binary digits ie. 1's and 0's incorporated in the background.

```html
<!DOCTYPE html>
<html lang="en">
<head>
<meta charset="utf-8">
<title>MR Systems (QLD) Pty Ltd – Business Card</title>
<link rel="stylesheet" href="https://fonts.googleapis.com/css2?family=Arimo:ital,wght@0,400;0,700;1,400&display=swap">
<style>
  :root {
    --page-bg: #e6e8ec;
    --blue-deep: #1553a6;
    --blue-mid: #2279cf;
    --blue-light: #4aa6ea;
    --cyan: #2aa3e2;
    --silver: #d9dde3;
    --grey-text: #9aa0a8;
    --ink: #1a1a1a;
    --name-blue: #1d6db9;
    --white: #ffffff;
  }
  * { margin: 0; padding: 0; box-sizing: border-box; }
  html, body { width: 1200px; height: 1044px; overflow: hidden; }
  body {
    background: var(--page-bg);
    font-family: "Arimo", Arial, sans-serif;
    position: relative;
  }
  .card {
    position: absolute;
    left: 222px;
    width: 756px;
    height: 420px;
    overflow: hidden;
    box-shadow: 0 6px 18px rgba(0,0,0,.18);
  }

  /* ---------- front ---------- */
  .card-front {
    top: 68px;
    background:
      radial-gradient(ellipse at 78% 18%, rgba(255,255,255,.35), transparent 55%),
      linear-gradient(160deg, var(--blue-light) 0%, var(--blue-mid) 45%, var(--blue-deep) 100%);
  }
  .front-swoosh { position: absolute; inset: 0; }
  .binary-field {
    position: absolute;
    left: 0; top: 40px;
    width: 360px; height: 360px;
    background: radial-gradient(ellipse at 20% 50%, rgba(120,190,245,.35), transparent 70%);
  }
  .front-brand {
    position: absolute;
    left: 0; right: 0; top: 130px;
    text-align: center;
    color: var(--silver);
  }
  .front-brand .brand-mark {
    font-size: 64px;
    font-weight: 400;
    letter-spacing: 1px;
  }
  .front-brand .brand-company {
    margin-top: 22px;
    font-size: 26px;
    letter-spacing: 2px;
  }
  .computer-art {
    position: absolute;
    right: 36px; bottom: 34px;
    width: 120px; height: 92px;
    border-radius: 6px;
    background: linear-gradient(180deg, #4a4f9a 0%, #c9ccd4 70%, #eef0f3 100%);
  }

  /* ---------- back ---------- */
  .card-back {
    top: 556px;
    background: linear-gradient(160deg, #ffffff 0%, #f1f2f4 100%);
  }
  .back-wave { position: absolute; inset: 0; }
  .back-brand {
    position: absolute;
    left: 40px; top: 26px;
    color: var(--grey-text);
  }
  .back-brand .brand-mark { font-size: 44px; }
  .back-brand .brand-company {
    margin-top: 10px;
    font-size: 17px;
    letter-spacing: 1px;
  }
  .contact {
    position: absolute;
    right: 40px; top: 150px;
    text-align: right;
  }
  .contact-name {
    color: var(--name-blue);
    font-size: 28px;
  }
  .contact-company {
    color: var(--ink);
    font-size: 19px;
    margin-top: 4px;
    letter-spacing: .5px;
  }
  .contact-lines {
    margin-top: 14px;
    display: grid;
    grid-template-columns: auto auto;
    column-gap: 6px;
    row-gap: 2px;
    text-align: left;
    font-size: 18px;
  }
  .contact-lines dt { color: var(--cyan); }
  .contact-lines dd { color: var(--ink); }
  .website {
    position: absolute;
    left: 40px; bottom: 30px;
    color: var(--white);
    font-size: 19px;
    letter-spacing: 4px;
  }
</style>
</head>
<body>

<section class="card card-front">
  <svg class="front-swoosh" viewBox="0 0 756 420" preserveAspectRatio="none" aria-hidden="true">
    <path d="M280 420 C420 260 560 160 756 110" fill="none" stroke="rgba(255,255,255,.25)" stroke-width="2"/>
    <path d="M360 420 C480 290 600 200 756 170" fill="none" stroke="rgba(255,255,255,.18)" stroke-width="3"/>
    <path d="M420 0 C520 80 640 110 756 100" fill="none" stroke="rgba(255,255,255,.2)" stroke-width="2"/>
  </svg>
  <div class="binary-field" role="img" aria-label="Faint binary digits background"></div>
  <div class="front-brand">
    <div class="brand-mark">MR Systems</div>
    <div class="brand-company">MR Systems (QLD) Pty Ltd</div>
  </div>
  <div class="computer-art" role="img" aria-label="Flat screen monitor, keyboard and mouse"></div>
</section>

<section class="card card-back">
  <svg class="back-wave" viewBox="0 0 756 420" preserveAspectRatio="none" aria-hidden="true">
    <defs>
      <linearGradient id="waveDeep" x1="0" y1="0" x2="1" y2="1">
        <stop offset="0" stop-color="#1c4f9c"/>
        <stop offset="1" stop-color="#1a7fc6"/>
      </linearGradient>
      <linearGradient id="waveCyan" x1="0" y1="0" x2="1" y2="0">
        <stop offset="0" stop-color="#1a8fd6"/>
        <stop offset="1" stop-color="#37b4ec"/>
      </linearGradient>
    </defs>
    <path d="M0 170 C110 260 300 350 756 372 L756 420 L0 420 Z" fill="url(#waveDeep)"/>
    <path d="M300 318 C470 350 620 372 756 382 L756 392 C600 386 440 366 300 318 Z" fill="#ffffff"/>
    <path d="M330 340 C500 380 630 394 756 396 L756 420 L420 420 Z" fill="url(#waveCyan)"/>
  </svg>

  <div class="back-brand">
    <div class="brand-mark">MR Systems</div>
    <div class="brand-company">MR Systems (QLD) Pty Ltd</div>
  </div>

  <div class="contact">
    <div class="contact-name">Dennis P Holtby</div>
    <div class="contact-company">MR Systems (QLD) Pty Ltd</div>
    <dl class="contact-lines">
      <dt>PO Box :</dt><dd>817 Harwick Point Qld 4619</dd>
      <dt>Mobile :</dt><dd>0412 739 064</dd>
      <dt>Mail&nbsp;&nbsp;&nbsp;&nbsp;:</dt><dd>programmer@mr-systems.example</dd>
    </dl>
  </div>

  <div class="website">www.mr-systems.example</div>
</section>

</body>
</html>
```